Premium men's gut health supplement needs a bottle label designed

We’re mossleaf - a premium men’s wellness brand focused on gut health. Our first product is a high-quality daily supplement designed to support digestion, regularity, and internal cleanliness. Backed by science and tailored for modern lifestyles, mossleaf is crafted in the UK and proudly LGBT-owned. It aims to resolve intimacy problems that gay men may experience due to poor digestion but also does not exclude any other orientation - other men may use it simply to improve their digestion.

mossleaf is for health-conscious men who value science-backed supplements and want to feel confident from the inside out. Many of our early adopters will be gay and bisexual men who prioritise gut health as part of their self-care, sexual, and hygiene routine, though the product is equally effective and appealing to anyone seeking premium digestive support.

The product is premium the target customer is male, not specific to one location but primary markets will be US, UK and EU.

I’d like a supplement bottle designed for mossleaf, our premium men’s gut health brand. The focus should be clean, slightly clinical, and minimal - inspired by brands like Varnō and Brek. The key element is the wordmark (mossleaf) on the front, with no additional logo or icon. Lowercase text and a strong, contemporary font are preferred.

The bottle should be aesthetically pleasing so that people are proud to display it on their shelf, instead of hiding it in a cupboard (like Varnō, brek, Ada Penrith, Olvanne etc)

Avoid anything that shows the product as being for LGBT, e.g., no rainbows, men holding hands etc.

The design should be premium, minimalist and not be busy or overwhelming.

I have uploaded a file called "Bottle" to give an idea of the type of container, but please ignore the colours and change as you see fit. This is just for reference for the type of bottle we'll use - all colours are customisable.

I have also uploaded some images for "style" reference, e.g., brek, varno, ada penrith, etc for inspiration.

```html
<!DOCTYPE html>
<html lang="en">
<head>
<meta charset="utf-8">
<title>mossleaf – Daily Digestive Support Supplement label</title>
<link rel="stylesheet" href="https://fonts.googleapis.com/css2?family=Montserrat:wght@400;600;700&display=swap">
<style>
  :root {
    --backdrop: #ebebeb;
    --label: #f8f1ef;
    --label-edge: #f1e6e4;
    --ink: #2b2b2b;
    --icon-tone: #d9cfcd;
  }
  * { margin: 0; padding: 0; box-sizing: border-box; }
  html, body {
    width: 1200px;
    height: 1200px;
    overflow: hidden;
    background: var(--backdrop);
  }
  .canvas {
    position: relative;
    width: 1200px;
    height: 1200px;
    display: flex;
    align-items: center;
    justify-content: center;
  }
  .label {
    position: relative;
    width: 760px;
    height: 930px;
    background: linear-gradient(90deg, var(--label-edge) 0%, var(--label) 25%, var(--label) 75%, var(--label-edge) 100%);
    color: var(--ink);
    font-family: "Montserrat", sans-serif;
    text-align: center;
  }
  .wordmark {
    position: absolute;
    top: 100px;
    left: 0;
    right: 0;
    font-size: 92px;
    font-weight: 700;
    letter-spacing: -1px;
    line-height: 1;
  }
  .product-type {
    position: absolute;
    top: 268px;
    left: 0;
    right: 0;
    font-size: 32px;
    font-weight: 400;
    line-height: 1.28;
    letter-spacing: 0.3px;
  }
  .icon-area {
    position: absolute;
    top: 430px;
    left: 50%;
    width: 230px;
    height: 230px;
    margin-left: -115px;
    border-radius: 50%;
    background: radial-gradient(circle, var(--icon-tone) 0%, var(--label) 72%);
  }
  .pack-info {
    position: absolute;
    top: 780px;
    left: 0;
    right: 0;
    font-size: 31px;
    line-height: 1.3;
  }
  .pack-info .count { font-weight: 700; }
  .pack-info .origin { font-weight: 400; }
</style>
</head>
<body>
  <main class="canvas">
    <section class="label">
      <h1 class="wordmark">mossleaf</h1>
      <p class="product-type">Daily Digestive<br>Support Supplement</p>
      <div class="icon-area" role="img" aria-label="Simple stomach pictogram"></div>
      <p class="pack-info">
        <span class="count">30 tablets</span><br>
        <span class="origin">Crafted in the UK</span>
      </p>
    </section>
  </main>
</body>
</html>
```